Australian Based Booking Platform Needs Playful Home Page & Profile Page To Showcase Our Acti...

COMPANY OVERVIEW:
WANDER-ON TICKETS is an Australian based activity booking platform. Our point of difference is our Kiosk machines that are located in hotels around Australia and allow customers instant access to book activities from the hotel reception.

HOME PAGE:
This page needs to clearly show that we are Australia’s leading booking platform.
Our Competition: https://www.roamplicity.com.au/en
IMPORTANT SECTIONS ON THE HOME PAGE:
- Key Bullet Points (Best Price Guaranteed, Trusted By Thousands, Australian Owned, Unbeatable Support)
- Top Experiences – (Images of selected experiences in a slider format)
- Take Me There – Gold Coast, Carins, Port Duglas, Sunshine Coast, Whitsundays, Brisbane, Sydney, Adelaide, Hobart, Perth
- Top Deals For You – (Images of selected experiences in a slider format)
- Experiences You’ll Love – (Categories of Adventure Tours, Outdoor Activities, Hot Deals, Fun & Games, Zoos & Aquariums, Reef & Island Cruises)
- Testimonials – (some sort of slider format)
- Top New Experience – (Images of selected experiences in a slider format)
- Footer Menu
NOTE: Including some sort of mascot on the page to introduce a personality would be amazing. A Kangaroo or Koala could be a good choice.

REGION PAGE:
This page needs to clearly show what is on offer in the region. The layout of this page will be used for all regions in Australia (eg Gold Coast, Carins, Port Duglas, Sunshine Coast, Whitsundays, Brisbane, Sydney, Adelaide, Hobart, Perth)
IMPORTANT SECTIONS ON THE REGION PAGE:
- Categories: Adventure Tours, Outdoor Activities, Hot Deals, Fun & Games, Zoos & Aquariums, Reef & Island Cruises
o This Categories menu allows you to flick between sliders with activities from the different categories
- Footer Menu

PROFILE PAGE:
The layout of this page is going to be used to clearly show off every activity people can book.
Competitors Example:
https://www.trekvane.com/tours/Sydney/Sydney-Harbour-Northern-beaches-and-National-Park/d482-559213K7
https://www.roamplicity.com.au/en/gold-coast/bellwick-isle-seal-and-corvana-reefs-snorkelling-cruise
IMPORTANT SECTIONS ON THE PROFILE PAGE:
- Tour Title
- Photos / Video
- Booking Calanda (As displayed on the above link)
- Highlights & Inclusions
- Overview
- Location (Map)
- What To Bring
- Additional Information
- Booking Information
- Reviews:
- Terms & Conditions
NOTE: This page is to be displayed on a kiosk with the following dimensions;
- 1209.8mm x 680.4mm
- Aspect Ratio 16:9

I have uploaded some images of Australia, as well as our logo. Please feel free to use or not use these images as you decide.
Updates

Keep up the good work on the designs :)

Target Market(s)

Australian Holiday Makers

Industry/Entity Type

Tourism Booking Platform

Number of Pages Required

3 page

Font styles to use
Sans Serif

Requirements
Must have
• - This booking calendar https://app.clipvault.com/kR7tWmZ2Lpq9
Nice to have
• A mascot or something to add character to the page.

```html
<!DOCTYPE html>
<html lang="en">
<head>
<meta charset="utf-8">
<title>Bellwick Isle Dolphin and Corvana Wrecks Snorkelling Tour – Wander-On Tickets</title>
<link href="https://fonts.googleapis.com/css2?family=Figtree:wght@400;500;600;700&display=swap" rel="stylesheet">
<style>
:root{
  --yellow:#f9c433;
  --yellow-deep:#f5b400;
  --ink:#111111;
  --text:#333333;
  --muted:#666666;
  --line:#e2e2e2;
  --card:#f6f6f6;
  --red:#d7262e;
  --hot:#f05a28;
  --footer:#000000;
  --footer-band:#2c2c2c;
  --white:#ffffff;
}
*{box-sizing:border-box;margin:0;padding:0}
html,body{width:1200px;height:2542px;overflow:hidden}
body{font-family:'Figtree',sans-serif;color:var(--text);background:var(--white);position:relative}
.hero-bg{position:absolute;left:0;top:0;width:1200px;height:340px}
.site-header{position:absolute;left:0;top:0;width:1200px;height:49px;background:var(--white)}
.brand{position:absolute;left:10px;top:16px;font-weight:700;font-size:14px;line-height:16px;color:var(--ink);letter-spacing:.3px;display:flex;align-items:center;gap:6px;white-space:nowrap}
.brand-dot{width:9px;height:9px;border-radius:50%;background:var(--yellow)}
.main-nav{position:absolute;left:228px;top:19px;display:flex;font-size:10px;color:var(--ink)}
.main-nav span{padding:0 18px;border-right:1px solid var(--ink);line-height:11px}
.main-nav span:first-child{padding-left:0}
.main-nav span:last-child{border:none}
.main-nav .hot{color:var(--hot)}
.login{position:absolute;left:1084px;top:12px;width:46px;height:24px;border-radius:12px;background:var(--yellow);font-size:9px;color:var(--ink);display:flex;align-items:center;justify-content:center}
.header-icon{position:absolute;top:15px}
.crumbs{position:absolute;left:203px;top:88px;font-size:8px;color:var(--ink)}
.tour-title{position:absolute;left:203px;top:113px;width:820px;font-size:29px;line-height:32px;font-weight:600;color:var(--ink)}
.tags{position:absolute;left:203px;top:193px;display:flex;gap:6px}
.tag{background:var(--ink);color:var(--white);font-size:8px;padding:2px 5px;border-radius:2px;height:14px;display:flex;align-items:center;gap:3px;white-space:nowrap}
.mascot{position:absolute;left:1072px;top:114px;width:128px;height:210px;border-radius:60px 60px 40px 40px;background:linear-gradient(160deg,#f3a93c,#e48a22)}
.thumb{position:absolute;left:203px;width:102px;height:65px;border-radius:8px}
.photo-main{position:absolute;left:313px;top:225px;width:400px;height:281px;border-radius:8px;background:linear-gradient(180deg,#2e2a3a 0%,#4a4260 40%,#8a6a58 70%,#2b2c3e 100%)}
.photo-next{position:absolute;left:690px;top:349px;width:23px;height:34px;background:var(--yellow);border-radius:6px 0 0 6px;display:flex;align-items:center;justify-content:center}
.booking-card{position:absolute;left:731px;top:225px;width:266px;height:236px;border:1px solid var(--line);border-radius:8px;background:var(--white);box-shadow:0 2px 8px rgba(0,0,0,.06)}
.sell-out{position:absolute;left:14px;top:12px;background:var(--red);color:var(--white);font-size:8.5px;padding:2px 5px;border-radius:3px}
.price{position:absolute;left:14px;top:32px;font-size:16.5px;font-weight:600;color:var(--ink)}
.price-note{position:absolute;left:14px;top:56px;font-size:7.5px;color:var(--muted)}
.field{position:absolute;height:25px;border:1px solid var(--line);border-radius:3px;font-size:9.5px;color:var(--ink);display:flex;align-items:center;white-space:nowrap}
.avail{position:absolute;left:14px;top:147px;width:238px;height:30px;background:var(--yellow);border-radius:4px;font-size:11px;font-weight:600;color:var(--ink);display:flex;align-items:center;justify-content:flex-end;padding-right:72px}
.grey-bar{position:absolute;left:14px;top:112px;width:238px;height:26px;background:#eeeeee;border-radius:3px}
.note-box{position:absolute;left:14px;top:186px;width:238px;height:36px;background:#fff6e0;border-radius:4px;font-size:8.5px;color:var(--text);padding:6px 0 0 140px;line-height:12px}
.calendar{position:absolute;left:742px;top:333px;width:144px;height:148px;background:var(--white);box-shadow:0 2px 8px rgba(0,0,0,.18);border-radius:3px;font-size:7.5px;color:var(--ink)}
.cal-head{display:flex;justify-content:space-between;padding:7px 9px 0}
.cal-grid{display:grid;grid-template-columns:repeat(7,18px);row-gap:5px;padding:6px 0 0 7px;text-align:center;line-height:12px}
.cal-grid .dow{font-weight:600}
.cal-grid .sel{background:var(--yellow);border-radius:50%}
.section-title{position:absolute;left:203px;font-size:21px;font-weight:600;color:var(--ink)}
.body-text{position:absolute;left:203px;width:512px;font-size:10.5px;line-height:16.3px;color:var(--text)}
.bullets{position:absolute;left:216px;width:500px;font-size:10.5px;line-height:16.8px;color:var(--text)}
.incl{position:absolute;display:flex;align-items:center;gap:8px;font-size:10.5px;color:var(--text);line-height:16px}
.tick{width:28px;height:28px;border:1.5px solid var(--yellow-deep);border-radius:50%;display:flex;align-items:center;justify-content:center;flex:none}
.address{position:absolute;left:203px;top:971px;display:flex;align-items:center;gap:8px;font-size:10.5px;color:var(--ink)}
.pin{width:28px;height:28px;border:1.5px solid var(--yellow-deep);border-radius:50%;display:flex;align-items:center;justify-content:center}
.map{position:absolute;left:203px;top:1010px;width:510px;height:281px;border-radius:10px;background:linear-gradient(90deg,#c9dcc0 0%,#d6e4cf 45%,#e9eaea 56%,#9dbbe9 62%,#9dbbe9 100%)}
.rating-row{position:absolute;left:203px;top:1697px;display:flex;align-items:center;gap:10px}
.stars{color:var(--yellow-deep);font-size:13px;letter-spacing:-1px}
.review{position:absolute;left:203px;width:510px;height:196px;background:var(--card);border:1px solid var(--line);border-radius:8px;padding:20px 18px}
.review-score{font-size:11px;color:var(--ink)}
.review-head{font-size:14.5px;line-height:18px;color:var(--ink);margin-top:13px}
.review-body{font-size:7.5px;line-height:11.3px;color:var(--text);margin-top:13px}
.review-by{font-size:6.5px;color:var(--muted);margin-top:9px}
.site-footer{position:absolute;left:0;top:2182px;width:1200px;height:360px;background:var(--footer);border-radius:26px 26px 0 0;color:var(--white)}
.footer-brand{position:absolute;left:53px;top:48px;width:140px;font-weight:700;font-size:12px;line-height:14px;white-space:nowrap;color:var(--white)}
.footer-col{position:absolute;top:49px}
.footer-col h4{font-size:12px;font-weight:500;margin-bottom:16px}
.footer-col li{list-style:none;font-size:8.5px;line-height:10px;margin-bottom:20.6px}
.social{position:absolute;top:2262px;width:28px;height:28px;border-radius:50%;background:#222;border:1px solid #3a3a3a}
.promo{position:absolute;left:1040px;top:2298px;width:106px;height:112px}
.promo-text{position:absolute;left:1052px;top:2340px;width:84px;text-align:center;font-size:8px;line-height:12px;font-weight:600;color:#3a2a00}
.ack{position:absolute;left:0;top:2475px;width:1200px;height:67px;background:var(--footer-band);font-size:8px;color:var(--white);padding:33px 0 0 53px}
</style>
</head>
<body>

<svg class="hero-bg" viewBox="0 0 1200 340" aria-hidden="true">
  <path fill="#f9c433" d="M0 49H1200V250C1150 220 1070 170 990 130C900 100 820 110 740 130C620 160 520 250 380 268C260 282 150 250 80 210C40 188 15 170 0 158Z"/>
</svg>

<header class="site-header">
  <div class="brand"><span>WANDER-ON TICKETS</span><span class="brand-dot"></span></div>
  <nav class="main-nav">
    <span>Destinations</span><span>Experiences</span><span class="hot">&#9679; Hot Deals</span><span>Gifts</span>
  </nav>
  <div class="login">Login</div>
  <svg class="header-icon" style="left:1138px" width="17" height="17" viewBox="0 0 17 17"><circle cx="7" cy="7" r="5.5" fill="none" stroke="#111" stroke-width="1.6"/><path d="M11 11l5 5" stroke="#111" stroke-width="1.6"/></svg>
  <svg class="header-icon" style="left:1168px" width="16" height="17" viewBox="0 0 16 17"><path d="M2 5h12l-1 11H3z" fill="none" stroke="#111" stroke-width="1.5"/><path d="M5 6V4a3 3 0 016 0v2" fill="none" stroke="#111" stroke-width="1.5"/></svg>
</header>

<div class="crumbs"><u>Home</u> &bull; <u>Profile</u></div>
<h1 class="tour-title">Bellwick Isle Dolphin and Corvana Wrecks Snorkelling Tour including Lunch</h1>
<div class="tags">
  <span class="tag">&#9733; Best seller</span><span class="tag">&#9632; Seasonal</span><span class="tag">&#9650; Meals included</span><span class="tag">&#9632; Hotel pickup</span><span class="tag">&#9679; Fitness level low</span><span class="tag">&#9679; Intensity level low</span>
</div>

<div class="mascot" role="img" aria-label="Kangaroo mascot illustration"></div>

<div class="thumb" style="top:225px;background:linear-gradient(180deg,#2b3a6b,#7b5a8a,#2c3a55)" role="img" aria-label="City skyline at night thumbnail"></div>
<div class="thumb" style="top:297px;background:linear-gradient(180deg,#6a87a8,#3c5a4a,#b9a58a)" role="img" aria-label="Palm trees on a beach thumbnail"></div>
<div class="thumb" style="top:369px;background:linear-gradient(180deg,#9fb3c6,#4a5f70,#2e5c84)" role="img" aria-label="Coastal city aerial thumbnail"></div>
<div class="thumb" style="top:441px;background:linear-gradient(180deg,#2e4566,#5a6a82,#3d3c48)" role="img" aria-label="City skyline at dusk thumbnail"></div>
<div class="photo-main" role="img" aria-label="Riverside city skyline lit up at night"></div>
<div class="photo-next"><svg width="10" height="16" viewBox="0 0 10 16"><path d="M2 1l7 7-7 7" fill="none" stroke="#111" stroke-width="1.5"/></svg></div>

<div class="booking-card">
  <span class="sell-out">Likely to Sell Out</span>
  <div class="price">From ₹21,142.60</div>
  <div class="price-note">Price varies by group size</div>
  <div class="field" style="left:14px;top:77px;width:146px;padding-left:10px;gap:14px">
    <svg width="11" height="11" viewBox="0 0 11 11"><rect x=".5" y="1.5" width="10" height="9" fill="none" stroke="#333"/><path d="M.5 4h10M3 0v3M8 0v3" stroke="#333"/></svg>
    <span>Sunday, Dec 17, 2023</span></div>
  <div class="field" style="left:167px;top:77px;width:85px;padding-left:10px;gap:30px">
    <svg width="10" height="11" viewBox="0 0 10 11"><circle cx="5" cy="3" r="2.6" fill="#333"/><path d="M0 11c0-4 2-5 5-5s5 1 5 5z" fill="#333"/></svg><span>1</span></div>
  <div class="grey-bar"></div>
  <div class="avail">bility</div>
  <div class="note-box">ours before the<br>)</div>
</div>

<div class="calendar">
  <div class="cal-head"><span>&lsaquo;</span><span>December 2023</span><span>&rsaquo;</span></div>
  <div class="cal-grid">
    <span class="dow">Su</span><span class="dow">Mo</span><span class="dow">Tu</span><span class="dow">We</span><span class="dow">Th</span><span class="dow">Fr</span><span class="dow">Sa</span>
    <span></span><span></span><span></span><span></span><span></span><span>1</span><span>2</span>
    <span>3</span><span>4</span><span>5</span><span>6</span><span>7</span><span>8</span><span>9</span>
    <span>10</span><span>11</span><span>12</span><span>13</span><span>14</span><span>15</span><span>16</span>
    <span class="sel">17</span><span>18</span><span>19</span><span>20</span><span>21</span><span>22</span><span>23</span>
    <span>24</span><span>25</span><span>26</span><span>27</span><span>28</span><span>29</span><span>30</span>
    <span>31</span>
  </div>
</div>

<h2 class="section-title" style="top:528px">Overview</h2>
<p class="body-text" style="top:564px">Take a day away from Sydney and head north: filled with beaches, historical sites, and Australian bushland. This private tour includes time to linger at Manly Beach and a stop at West Head Lookout in Ku-Ring-Gai Chase National Park to view aboriginal rock art. At Palm Beach we visit Barrenjoey Lighthouse and have a nutritious lunch. We then have a brief stop at Avalon and Bilgola Beaches, and catch a return ferry on Sydney Harbour from Manly. The day covers a lot of ground, with exceptional scenery.</p>
<ul class="bullets" style="top:670px">
  <li>Private day trip traverses Sydney Harbour to picturesque northern beaches</li>
  <li>Explore aboriginal rock art at Ku-ring-gai Chase National Park</li>
  <li>Marvel at a viewpoint panorama over Lion Island and the Palm Beach isthmus</li>
  <li>Personal guide provides options to customize your sightseeing</li>
</ul>

<h2 class="section-title" style="top:760px">Highlights &amp; inclusions</h2>
<div class="incl" style="left:203px;top:804px"><span class="tick"><svg width="12" height="10" viewBox="0 0 12 10"><path d="M1 5l3.5 3.5L11 1" fill="none" stroke="#111" stroke-width="1.4"/></svg></span>Visit iconic Bellwick Isle</div>
<div class="incl" style="left:458px;top:804px"><span class="tick"><svg width="12" height="10" viewBox="0 0 12 10"><path d="M1 5l3.5 3.5L11 1" fill="none" stroke="#111" stroke-width="1.4"/></svg></span>Swimming and snorkelling</div>
<div class="incl" style="left:203px;top:839px"><span class="tick"><svg width="12" height="10" viewBox="0 0 12 10"><path d="M1 5l3.5 3.5L11 1" fill="none" stroke="#111" stroke-width="1.4"/></svg></span>See colourful sub-tropical fish</div>
<div class="incl" style="left:458px;top:839px"><span class="tick"><svg width="12" height="10" viewBox="0 0 12 10"><path d="M1 5l3.5 3.5L11 1" fill="none" stroke="#111" stroke-width="1.4"/></svg></span>See the Corvana Wrecks</div>
<div class="incl" style="left:203px;top:875px"><span class="tick"><svg width="12" height="10" viewBox="0 0 12 10"><path d="M1 5l3.5 3.5L11 1" fill="none" stroke="#111" stroke-width="1.4"/></svg></span>Enjoy a delicious tropical lunch</div>
<div class="incl" style="left:458px;top:873px"><span class="tick"><svg width="12" height="10" viewBox="0 0 12 10"><path d="M1 5l3.5 3.5L11 1" fill="none" stroke="#111" stroke-width="1.4"/></svg></span>Transfers from Brisbane or Gold Coast<br>available</div>

<h2 class="section-title" style="top:933px">Location</h2>
<div class="address"><span class="pin"><svg width="12" height="14" viewBox="0 0 12 14"><path d="M6 13S1 8 1 5a5 5 0 0110 0c0 3-5 8-5 8z" fill="none" stroke="#111" stroke-width="1.3"/><circle cx="6" cy="5" r="1.8" fill="none" stroke="#111" stroke-width="1.3"/></svg></span><u>42 Harbourline Drive, Kelmora, QLD 4190</u></div>
<div class="map" role="img" aria-label="Map of the Gold Coast region showing the tour departure point"></div>

<h2 class="section-title" style="top:1318px">Additional Info</h2>
<ul class="bullets" style="top:1350px">
  <li>Confirmation will be received at time of booking.</li>
  <li>Travelers should have a moderate physical fitness level.</li>
  <li>Not wheelchair accessible.</li>
  <li>This is a private tour/activity. Only your group will participate.</li>
  <li>No heart problems or other serious medical conditions.</li>
</ul>

<h2 class="section-title" style="top:1458px">Cancellation Policy</h2>
<p class="body-text" style="top:1494px">You can cancel up to 24 hours in advance of the experience for a full refund.</p>
<ul class="bullets" style="top:1519px">
  <li>For a full refund, you must cancel at least 24 hours before the experience’s start time.</li>
  <li>Cut-off times are based on the experience’s local time.</li>
  <li>If you cancel less than 24 hours before the experience’s start time, the amount you paid will not be refunded.</li>
  <li>This experience requires good weather. If it’s canceled due to poor weather, you’ll be offered a different date or a full refund.</li>
  <li>Any changes made less than 24 hours before the experience’s start time will not be accepted.</li>
</ul>

<h2 class="section-title" style="top:1661px">Recent Reviews</h2>
<div class="rating-row"><span class="stars">&#9733;&#9733;&#9733;&#9733;&#9733;</span><span style="font-size:13px;color:#111">4.6</span><span style="font-size:8.5px;color:#666">34 reviews</span></div>

<article class="review" style="top:1722px">
  <div class="review-score">&#9733; 4.6</div>
  <div class="review-head">Well organised tour, enthusiastic staff and amazing content. Had a beautiful morning tea and lunch on the boat. All snorkel gear and kayak included. Beach was stunning</div>
  <div class="review-body">Loved the day out with the family. We got to see a dugong and many dolphins in their natural habitat as well as turtles. Beautiful reef and fish on the shipwrecks. Day was well organised and co-ordinated by the crew from the start. Enjoyed the lunch and happy hour on offer. Very comfortable the whole way through.</div>
  <div class="review-by">Lena Corwell 8 months ago</div>
</article>
<article class="review" style="top:1930px">
  <div class="review-score">&#9733; 4.2</div>
  <div class="review-head">Well organised tour, enthusiastic staff and amazing content. Had a beautiful morning tea and lunch on the boat. All snorkel gear and kayak included. Beach was stunning</div>
  <div class="review-body">Loved the day out with the family. We got to see a dugong and many dolphins in their natural habitat as well as turtles. Beautiful reef and fish on the shipwrecks. Day was well organised and co-ordinated by the crew from the start. Enjoyed the lunch and happy hour on offer. Very comfortable the whole way through.</div>
  <div class="review-by">Lena Corwell 8 months ago</div>
</article>

<footer class="site-footer">
  <div class="footer-brand">WANDER-ON TICKETS</div>
  <div class="footer-col" style="left:209px"><h4>Join Us</h4><ul><li>Affiliate Partners</li><li>Experience Operators</li><li>Careers</li><li>Let's Collaborate</li></ul></div>
  <div class="footer-col" style="left:409px"><h4>Our Company</h4><ul><li>About Us</li><li>FAQs</li><li>Blogs</li><li>Privacy Policy</li><li>Terms and Conditions</li><li>Security</li></ul></div>
  <div class="footer-col" style="left:609px"><h4>Get In Touch</h4><ul><li>Contact Us</li><li>Press Room</li><li>Visit The Experience Centre</li></ul></div>
</footer>
<span class="social" style="left:1034px"></span>
<span class="social" style="left:1074px"></span>
<span class="social" style="left:1115px"></span>
<svg class="promo" viewBox="0 0 106 112" aria-hidden="true"><path fill="#f9c433" d="M60 4C72 -2 88 6 90 22C104 40 106 62 92 82C84 94 76 100 70 104L72 112L62 104C44 104 30 106 18 96C4 86 0 66 6 48C12 30 30 24 44 26C50 14 54 8 60 4Z"/></svg>
<div class="promo-text">Pssst, there's $10 waiting for you. Join for free today.</div>
<div class="ack">We acknowledge and pay respect to the Traditional Custodians of Country and their connections and continuous care for the skies, lands and waterways throughout Australia.</div>

</body>
</html>
```